Boom Way Hoist Service Business Cards

I need a business card for "Boom Way Hoist and Haulage"

Boomway2023@hoistmail.net

Hoist Works LLC, Boom Way Hoist and Haulage LLC

555.014.7260 | www.BOOMWAYHOISTS.example

Central Indiana & Northeast Ohio

(IN) 14820 Maple Lane Noblesville, IN 46000

(OH) 2450 Pell Street Akron, Ohio 44300

Colors
0094D4
00A9DD
6FCCEA
C7EBF8
E9F6FB
59FF00
82FF00
B8FF75
E3FFCB
F4FFEA
EE7325
F08F49
F5BC92
FAE3D3
FDF4ED
EB3D1F
EC4F4E
F09395
F8D3D4
FCEDEE
E54698
E96AAD
F1A4CE
F9D9EA
FCEFF6
A7469A
B969AE
D3A5CF
EDDBEB
F8F0F9

```html
<!DOCTYPE html>
<html lang="en">
<head>
<meta charset="utf-8">
<title>Boom Way Hoist and Haulage — Business Card</title>
<link rel="stylesheet" href="https://fonts.googleapis.com/css2?family=Orbitron:wght@800&family=PT+Sans:wght@400;700&display=swap">
<style>
  :root {
    --backdrop: #9b9b9b;
    --card-black: #000000;
    --card-white: #ffffff;
    --brand-green: #33c43f;
    --ink: #1e1e1e;
    --light: #ffffff;
  }
  * { box-sizing: border-box; margin: 0; padding: 0; }
  html, body {
    width: 1093px;
    height: 1200px;
    overflow: hidden;
    background: var(--backdrop);
  }
  .canvas {
    position: relative;
    width: 1093px;
    height: 1200px;
  }
  .card {
    position: absolute;
    left: 264px;
    width: 580px;
    height: 358px;
    overflow: hidden;
  }
  .card--front { top: 226px; background: var(--card-white); }
  .card--back { top: 620px; height: 361px; background: var(--card-black); }

  .front__band {
    position: absolute;
    left: 0; top: 0;
    width: 100%;
    height: 167px;
    background: var(--card-black);
  }
  .front__rule {
    position: absolute;
    left: 0; top: 172px;
    width: 302px;
    height: 4px;
    background: var(--brand-green);
  }
  .entities {
    position: absolute;
    left: 27px; top: 54px;
    font-family: "Orbitron", sans-serif;
    font-weight: 800;
    font-size: 15px;
    line-height: 23px;
    text-transform: uppercase;
    letter-spacing: 1px;
  }
  .entities__primary { color: var(--brand-green); }
  .entities__secondary { color: var(--light); }

  .brand-name {
    font-family: "Orbitron", sans-serif;
    font-weight: 800;
    color: var(--brand-green);
    text-transform: uppercase;
    letter-spacing: 0.5px;
  }
  .front__brand {
    position: absolute;
    right: 22px; top: 122px;
    font-size: 12px;
    line-height: 17px;
    text-align: right;
  }

  .details {
    position: absolute;
    left: 27px; top: 198px;
    font-family: "PT Sans", sans-serif;
    color: var(--ink);
  }
  .details__region {
    color: var(--brand-green);
    font-size: 16.5px;
    font-weight: 700;
    margin-bottom: 10px;
  }
  .details__address {
    font-size: 16px;
    line-height: 22px;
  }
  .contact {
    position: absolute;
    left: 27px; top: 297px;
    display: flex;
    gap: 9px;
    align-items: center;
    font-family: "PT Sans", sans-serif;
    font-size: 13px;
    color: var(--ink);
    white-space: nowrap;
  }
  .contact__item { display: flex; align-items: center; gap: 4px; }
  .contact__icon { width: 13px; height: 13px; flex: none; }
  .contact__accent { color: var(--brand-green); }

  .back__brand {
    position: absolute;
    left: 0; right: 0; top: 150px;
    text-align: center;
    font-size: 22px;
    line-height: 34px;
  }
</style>
</head>
<body>
<main class="canvas">
  <section class="card card--front" aria-label="Business card front">
    <div class="front__band"></div>
    <div class="front__rule"></div>
    <div class="entities">
      <p class="entities__primary">Hoist Works LLC</p>
      <p class="entities__secondary">Boom Way Hoist and<br>Haulage LLC</p>
    </div>
    <p class="brand-name front__brand">Boom Way<br>Hoist and Haulage</p>

    <div class="details">
      <p class="details__region">Central Indiana &amp; Northeast Ohio</p>
      <p class="details__address">(IN) 14820 Maple Lane Noblesville, IN 46000</p>
      <p class="details__address">(OH) 2450 Pell Street Akron, Ohio 44300</p>
    </div>

    <div class="contact">
      <span class="contact__item">
        <svg class="contact__icon" viewBox="0 0 24 24" aria-hidden="true"><path fill="#33c43f" d="M6.6 10.8a15.1 15.1 0 0 0 6.6 6.6l2.2-2.2c.3-.3.7-.4 1-.2 1.1.4 2.3.6 3.6.6.6 0 1 .4 1 1V20c0 .6-.4 1-1 1A17 17 0 0 1 3 4c0-.6.4-1 1-1h3.5c.6 0 1 .4 1 1 0 1.3.2 2.5.6 3.6.1.3 0 .7-.2 1z"/></svg>
        <span>555.014.7260</span>
      </span>
      <span class="contact__item">
        <svg class="contact__icon" viewBox="0 0 24 24" aria-hidden="true"><rect x="2" y="5" width="20" height="14" fill="#33c43f"/><path d="M2 5l10 8 10-8" fill="none" stroke="#fff" stroke-width="1.6"/></svg>
        <span>Boomway2023@hoistmail.net</span>
      </span>
      <span class="contact__item">
        <svg class="contact__icon" viewBox="0 0 24 24" aria-hidden="true"><g fill="none" stroke="#33c43f" stroke-width="2"><circle cx="12" cy="12" r="9"/><ellipse cx="12" cy="12" rx="4" ry="9"/><path d="M3 12h18M5 7h14M5 17h14"/></g></svg>
        <span>www.<span class="contact__accent">BOOMWAYHOISTS</span>.example</span>
      </span>
    </div>
  </section>

  <section class="card card--back" aria-label="Business card back">
    <p class="brand-name back__brand">Boom Way<br>Hoist and Haulage</p>
  </section>
</main>
</body>
</html>
```